Webdesign für Augenarztpraxis gesucht
Zielgruppe
Augenarztpraxis, Zielgruppe: Patienten, Interessenten
Aufgabenstellung
Liebe Designer, liebe Designerinnen,
es handelt sich hierbei um keinen Design-Contest, eher um eine Ausschreibung.
anbei die konkrete Projektinalte:
- bestehende HP http://www.sehzentrum-lindmoor.de moderner gestalten
- Aufbau und Inhalte können übernommen werden, nur Austausch von alten Bildern (Fotoshooting geplant)
- ergänzend: Bildlizenzen / Stockfotografie
- Aufbau aller Seiten und Unterseiten
- SEO/SEA Googleanpassungen – Implementierung relevanter Suchbegriffe
- eventuell kleine Textanpassungen
- gehostetes CMS, geringe Wartungskosten
- DSGVO konformes Impressum und Datenschutzseite
- Technische Abwicklung mit dem Hoster
Bitte um Nennung der Kosten (siehe oben):
- Gesamtkosten Umgestaltung der HP
- Kosten CMS Hosting
- sonstige Wartungskosten
- Stundensatz für sonstige Programmierleistungen
- Stundensatz für das Sichten der gelieferten Texte, anpassen und Neuanpassung der Texte pro Seite
Wichtig: bitte geben Sie Referenzen an, um die Vorauswahl zu erleichtern
Vielen Dank!
brunowaldau@postfeld.de
- es soll die bestehende HP: http://blickhaus-falkenau.de/team.html moderner gestaltet werden
- die meißten Inhalte können von der aktuellen HP: http://blickhaus-falkenau.de/team.html übernommen werden
- neue Praxis- und Mitarbeiterfotos werden durch einen Fotografen neu erstellt (Auftrag ist noch zu vergeben)
- Wichtig: bitte geben Sie unbedingt Referenzen an, um die Vorauswahl zu erleichtern
- bitte auch um die Angabe von Preisen für spätere Änderungen bezügl. Inhalte und Aufbau

```html
<!DOCTYPE html>
<html lang="de">
<head>
<meta charset="utf-8">
<title>Blickhaus Falkenau</title>
<link rel="stylesheet" href="https://fonts.googleapis.com/css2?family=Source+Sans+3:wght@400;600;700&display=swap">
<style>
  :root {
    --navy: #21214f;
    --ink: #1c1c1c;
    --muted: #5e5e5e;
    --paper: #ffffff;
    --shadow: rgba(0,0,0,0.22);
  }
  * { box-sizing: border-box; margin: 0; padding: 0; }
  html, body { width: 899px; height: 1200px; overflow: hidden; background: var(--paper); }
  body { position: relative; font-family: "Source Sans 3", sans-serif; color: var(--ink); }

  .site-header {
    position: absolute; left: 4px; top: 4px; width: 891px; height: 177px;
    background: var(--paper); border-top: 6px solid var(--navy);
    box-shadow: 0 1px 3px var(--shadow);
  }
  .brand { position: absolute; left: 120px; top: 22px; display: flex; align-items: center; gap: 10px; }
  .brand-dot { width: 30px; height: 30px; border-radius: 50%; background: var(--ink); }
  .brand-name { font-size: 26px; font-weight: 700; letter-spacing: 0.3px; color: var(--ink); text-transform: uppercase; }
  .doctors { position: absolute; left: 161px; top: 57px; list-style: none; font-size: 12px; letter-spacing: 0.4px; line-height: 20.5px; text-transform: uppercase; }
  .main-nav { position: absolute; top: 147px; left: 0; width: 100%; }
  .main-nav a { position: absolute; font-size: 11px; letter-spacing: 0.8px; color: var(--ink); text-decoration: none; }

  .section-title { position: absolute; left: 165px; font-size: 16.5px; font-weight: 600; letter-spacing: 0.3px; }
  .intro { position: absolute; left: 165px; top: 265px; width: 357px; font-size: 11.4px; line-height: 17.6px; text-align: justify; }

  .card-button, .accordion {
    position: absolute; left: 163px; height: 35px; background: var(--paper);
    box-shadow: 0 1px 3px var(--shadow); border: 1px solid #ececec;
    display: flex; align-items: center; justify-content: space-between;
    padding: 0 13px 0 11px; font-size: 13px; letter-spacing: 0.3px;
  }
  .card-button { top: 398px; width: 257px; font-weight: 700; }
  .accordion { width: 190px; }
  .accordion.wide { width: 371px; }
  .caret { width: 6px; height: 6px; }

  .info-box { position: absolute; left: 564px; width: 171px; background: var(--paper); box-shadow: 0 1px 3px var(--shadow); }
  .info-box h2 { background: var(--navy); color: #fff; font-size: 15px; font-weight: 600; letter-spacing: 0.5px; text-align: center; height: 35px; line-height: 35px; border-radius: 2px 2px 0 0; }
  .hours { top: 268px; height: 165px; }
  .hours dl { display: grid; grid-template-columns: 58px 1fr; padding: 9px 0 0 12px; font-size: 11.5px; line-height: 17px; }
  .hours dt { font-weight: 700; }
  .hours .gap { margin-top: 16px; }
  .hours .note { padding: 13px 0 0 12px; font-size: 11.5px; font-weight: 600; }
  .address { top: 442px; height: 82px; }
  .address p { text-align: center; font-size: 11.5px; font-weight: 600; line-height: 16.5px; padding-top: 8px; }
</style>
</head>
<body>
  <header class="site-header">
    <div class="brand">
      <span class="brand-dot"></span>
      <span class="brand-name">Blickhaus Falkenau</span>
    </div>
    <ul class="doctors">
      <li>Priv.-Doz. Dr. Henrik Albrecht</li>
      <li>Dr. Marlene Kessler</li>
      <li>Dr. Johanna Albrecht</li>
    </ul>
    <nav class="main-nav">
      <a href="#" style="left:161px">Home</a>
      <a href="#" style="left:251px">Leistungen</a>
      <a href="#" style="left:368px">Diagnosen</a>
      <a href="#" style="left:485px">Team</a>
      <a href="#" style="left:571px">Kontakt</a>
      <a href="#" style="left:672px">Impressum</a>
    </nav>
  </header>

  <h1 class="section-title" style="top:216px">Herzlich Willkommen</h1>
  <p class="intro">Seit unserem Bestehen haben wir weit über 55.000 Operationen mit höchster Präzision durchgeführt. Dabei ist selbstverständlich unser oberstes Ziel die Zufriedenheit unserer Patientinnen und Patienten. Nach einer ausführlichen Diagnostik mit modernsten Geräten und einer individuellen Beratung führen wir ambulante Operationen und Behandlungen in einem breiten Spektrum durch.</p>
  <a class="card-button" href="#">Vereinbaren Sie direkt einen Termin
    <svg class="caret" viewBox="0 0 6 6"><path d="M1 0 L5 3 L1 6 Z" fill="#1c1c1c"/></svg>
  </a>

  <aside class="info-box hours">
    <h2>Sprechzeiten</h2>
    <dl>
      <dt>Mo. - Fr.:</dt><dd>08:00 - 12:00 Uhr</dd>
      <dt>Mo. - Do.:</dt><dd>15:00 - 17:00 Uhr</dd>
      <dt class="gap">Telefon:</dt><dd class="gap">04712-530 84</dd>
      <dt>Fax:</dt><dd>04712-530 849</dd>
    </dl>
    <p class="note">Termine nach Vereinbarung</p>
  </aside>
  <aside class="info-box address">
    <h2>Adresse</h2>
    <p>Lindenallee 12-14<br>27301 Falkenau</p>
  </aside>

  <h2 class="section-title" style="top:557px">Diagnosen, die Sie kennen sollten</h2>
  <div class="accordion" style="top:605px">Grauer Star (Cateract)<svg class="caret" viewBox="0 0 6 6"><path d="M0 1 L6 1 L3 5 Z" fill="#1c1c1c"/></svg></div>
  <div class="accordion" style="top:673px">Grüner Star (Glaukom)<svg class="caret" viewBox="0 0 6 6"><path d="M0 1 L6 1 L3 5 Z" fill="#1c1c1c"/></svg></div>
  <div class="accordion" style="top:740px">Maculadegeneration<svg class="caret" viewBox="0 0 6 6"><path d="M0 1 L6 1 L3 5 Z" fill="#1c1c1c"/></svg></div>
  <div class="accordion" style="top:808px">Kurz-/ Weitsichtigkeit<svg class="caret" viewBox="0 0 6 6"><path d="M0 1 L6 1 L3 5 Z" fill="#1c1c1c"/></svg></div>

  <h2 class="section-title" style="top:902px">Unsere Leistungen im Überblick</h2>
  <div class="accordion wide" style="top:961px">Ambulante Operationen<svg class="caret" viewBox="0 0 6 6"><path d="M0 1 L6 1 L3 5 Z" fill="#1c1c1c"/></svg></div>
  <div class="accordion wide" style="top:1029px">Intravitreale operative Medikamenteneingabe (IVOM)<svg class="caret" viewBox="0 0 6 6"><path d="M0 1 L6 1 L3 5 Z" fill="#1c1c1c"/></svg></div>
</body>
</html>
```